Stationery Set for BRV Company

I need to create full stationery design for my company; Business Cards, Envelops, Letter Heads, Calendar.
In the letter head and Envelops... only contact information and website links.
Our company is a Service Management company with different domains of innovative services including Technology Service Management, Education Services, Outsourcing Management, Events Management.
I need a modern and innovative design specially for the business card. I some transparent designs and I like it, but don't limit your innovation to what I mentioned. Sky is limit for your innovation.

Target Market(s)

Middle East & Africa

Industry/Entity Type

Business Management

Colors
34a7d8
0355a3
85acd3
86cae7
cee9f5
cfdeed
e4daeb
f3f1f8
ecf7fb

Requirements
Must have
• Name, Title, Email, Mobile
Nice to have
• We have multiple locations in USA, KSA, EGY, so I need ideas about how to include all contact details maybe QR / Barcode or something else.
• Please see our locations and contact information: www.ploventa.com
Should not have
• Too much text

```html
<!DOCTYPE html>
<html lang="en">
<head>
<meta charset="utf-8">
<title>BRV Company – Business Card</title>
<link rel="stylesheet" href="https://fonts.googleapis.com/css2?family=Open+Sans:wght@400;600;700&display=swap">
<style>
  :root{
    --brand-blue:#3d6fbf;
    --panel-white:#ffffff;
    --panel-edge:#cbc5c2;
    --mark-grey:#b9b2ae;
    --stage:#e9e9ec;
    --ink-white:#ffffff;
  }
  *{margin:0;padding:0;box-sizing:border-box}
  html,body{width:1200px;height:750px;overflow:hidden;background:var(--stage);font-family:"Open Sans",Arial,sans-serif}
  .canvas{position:relative;width:1200px;height:750px}
  .card{position:absolute;top:226px;width:520px;height:297px;border-radius:3px;overflow:hidden;box-shadow:0 6px 18px rgba(0,0,0,.18)}
  .card--front{left:50px;background:var(--panel-white)}
  .card--back{left:630px;background:var(--brand-blue);color:var(--ink-white)}
  .wordmark{position:absolute;display:flex;align-items:center;gap:10px;font-weight:700;color:var(--brand-blue);white-space:nowrap}
  .wordmark__square{width:18px;height:18px;background:var(--mark-grey)}
  .card--front .wordmark{left:50%;top:50%;transform:translate(-50%,-50%);font-size:40px}
  .card--back .wordmark{left:268px;top:44px;font-size:30px}
  .card--back .wordmark__square{width:14px;height:14px}
  .panel{position:absolute;inset:0}
  .holder{position:absolute;left:30px;top:106px}
  .holder__name{font-size:18px;font-weight:700;line-height:1.1}
  .holder__title{font-size:12px;font-weight:400;margin-top:2px}
  .office{position:absolute;font-size:9.5px;line-height:1.4}
  .office__country{font-weight:700}
  .office__phone{font-weight:700}
  .office--ksa{left:30px;top:200px}
  .office--usa{left:228px;top:186px}
  .contacts{position:absolute;left:392px;top:186px;list-style:none;font-size:9.5px;line-height:1.7}
  .contacts li{display:flex;align-items:center;gap:6px}
  .contacts svg{width:10px;height:10px;flex:none}
</style>
</head>
<body>
<main class="canvas">

  <section class="card card--front" aria-label="Business card front">
    <div class="wordmark"><span class="wordmark__square"></span>BRV Company</div>
  </section>

  <section class="card card--back" aria-label="Business card back">
    <svg class="panel" viewBox="0 0 520 297" aria-hidden="true">
      <path d="M196 0 H520 V122 L266 172 Q232 178 224 146 L196 0 Z" fill="var(--panel-edge)"/>
      <path d="M192 0 H520 V116 L262 166 Q229 172 221 140 L192 0 Z" fill="var(--panel-white)"/>
    </svg>
    <div class="wordmark"><span class="wordmark__square"></span>BRV Company</div>

    <div class="holder">
      <p class="holder__name">Omar Haddad</p>
      <p class="holder__title">President</p>
    </div>

    <address class="office office--ksa" style="font-style:normal">
      <p class="office__country">SAUDI ARABIA:</p>
      <p>Riyadh, Al Nakheel,</p>
      <p>Prince Faisal St.</p>
      <p>Rawabi Towers</p>
      <p>Block 4C 3rd Floor C12, C14</p>
      <p class="office__phone">Phone : +966 11 555 0143</p>
    </address>

    <address class="office office--usa" style="font-style:normal">
      <p class="office__country">USA:</p>
      <p>418 Harbor Point Way</p>
      <p>4th Floor Bayview City</p>
      <p>CA 94120 US</p>
      <p class="office__phone">Phone : +1.4155550182</p>
    </address>

    <ul class="contacts">
      <li><svg viewBox="0 0 10 10"><rect x="2.5" y="0.5" width="5" height="9" rx="1" fill="none" stroke="#fff"/></svg>+1.4155550182</li>
      <li><svg viewBox="0 0 10 10"><rect x="0.5" y="2" width="9" height="6" fill="#fff"/><path d="M0.5 2 L5 5.5 L9.5 2" fill="none" stroke="var(--brand-blue)" stroke-width="0.8"/></svg>info@ploventa.com</li>
      <li><svg viewBox="0 0 10 10"><circle cx="5" cy="5" r="4.5" fill="#fff"/><path d="M0.5 5 H9.5 M5 0.5 V9.5" stroke="var(--brand-blue)" stroke-width="0.6"/></svg>www.ploventa.com</li>
    </ul>
  </section>

</main>
</body>
</html>
```